CBD OIl Label and Brand Design

**UPDATE** Can't say CBD anywhere on the label / box. Must only use Hemp Oil Extract instead. THANK YOU!
Hi. Thank you for looking at my task. Looking to create a Day and Night Product line. White bottle for Day product, Black Bottle for Night Product.
Day Product name = Vantor (Lightning bolt energy icon)
Night Product name = Mirel (Moon Icon)
This is to create a very nice CBD Oil label design. It will be on a 30ml glass dropper bottle. White bottle and black bottle. White box, and black box.
VERY SIMPLE and CLEAN. Minimalist approach. I want a clear label on white bottle. And a clear label on a black bottle. Bottle will be inside of a box. Details on the box exactly same as label + barcode.
Key text information to be on the front of the label (center).
Possible Brand Name: Zeb, Opal Crest (Opl Crst), KLDR, Bravi Wellness Hemp.
1500mg
Full Spectrum Hemp Oil Extract
Non-Psychoactive
Smaller at bottom: 30ml
Right side of label and box:
Supplement Facts
Serving Size: 1ml dropper
Servings per container: 30
-
Amount Per Serving %DV
Hemp Oil Extract **50mg
2mg appox per drop **
-
** \Daily Value not established
Please do not have lines around the Supplement facts area or lines in between. See image example. Clean and simple look!!
Other Ingredients: MCT Oil (Fractinated Coconut Oil). Infused Terpenes.
Left Side of Label and Box:
Directions: Shake Well Before Use. (bold)
For sublingual use: 0.25ml to 1ml daily placed under tongue for at least 10 seconds before swallowing.
BRO Warning Box
*These statements have not been evaluated by the Bureau of Remedy Oversight. This product is not intended to diagnose, treat, cure, or prevent any disease.
Please consult your health care professional about potential interactions or other possible complications before using this product.
Must be 18 years or older to purchase.
Box Only Not on Label:
Manufactured for:
Pemberly Supply, LLC
5678 Pemberly Loop Dr.
Tigard, OR 97224
866-555-0147
www.quillorbay-example.com
Barcode can go on BOX. Not on label.
Security emblems on box:
Made in USA
NO THC
Cruelty Free
Updates
Designs look the same
Target Market(s)
Mid 30s - 40s looking to benefit their health and take care of their bodies while trying to build out their prime career years.
Industry/Entity Type
Health And Wellness
Look and feel
Each slider illustrates characteristics of the customer's brand and the style your logo design should communicate.

```html
<!DOCTYPE html>
<html lang="en">
<head>
<meta charset="utf-8">
<title>Zeb Hemp Oil Extract – Day and Night Labels</title>
<link rel="stylesheet" href="https://fonts.googleapis.com/css2?family=Poppins:wght@300;400&family=Oswald:wght@500;600&display=swap">
<style>
  :root {
    --canvas: #ffffff;
    --frame: #1a1a1a;
    --label-day: #ffffff;
    --label-night: #050505;
    --ink-day: #111111;
    --ink-night: #ffffff;
    --lime: #9be41c;
    --shadow: rgba(0, 0, 0, 0.12);
  }
  * { box-sizing: border-box; margin: 0; padding: 0; }
  html, body { width: 1064px; height: 1200px; overflow: hidden; background: var(--canvas); }
  .canvas {
    width: 1064px; height: 1200px;
    border: 2px solid var(--frame);
    display: flex; justify-content: center; align-items: center; gap: 80px;
  }
  .label {
    width: 340px; height: 500px;
    display: flex; flex-direction: column; align-items: center;
    padding-top: 34px;
    box-shadow: 0 2px 10px var(--shadow);
  }
  .label--day { background: var(--label-day); color: var(--ink-day); }
  .label--night { background: var(--label-night); color: var(--ink-night); }
  .brand {
    font-family: "Poppins", sans-serif; font-weight: 400;
    font-size: 34px; letter-spacing: 3px; line-height: 1;
  }
  .strength {
    margin-top: 42px;
    font-family: "Poppins", sans-serif; font-weight: 300;
    font-size: 20px; color: var(--lime); line-height: 1;
  }
  .spectrum {
    margin-top: 4px;
    font-family: "Oswald", sans-serif; font-weight: 500;
    font-size: 30px; line-height: 1.1; transform: scaleX(0.82);
  }
  .product {
    margin-top: 18px; width: 214px;
    border-top: 2px solid currentColor; border-bottom: 2px solid currentColor;
    padding: 6px 0 4px; text-align: center;
  }
  .product__kind {
    font-family: "Poppins", sans-serif; font-weight: 300;
    font-size: 42px; color: var(--lime); line-height: 1; letter-spacing: -0.5px;
    white-space: nowrap;
  }
  .product__form {
    font-family: "Oswald", sans-serif; font-weight: 600;
    font-size: 44px; line-height: 1.05; letter-spacing: 6px; margin-right: -6px;
    white-space: nowrap;
  }
  .variant-mark {
    margin-top: 36px; width: 48px; height: 52px;
    border-radius: 6px; background: var(--lime); opacity: 0.85;
  }
  .claim {
    margin-top: 30px;
    font-family: "Oswald", sans-serif; font-weight: 600;
    font-size: 13px; letter-spacing: 2px;
  }
  .volume {
    margin-top: 6px;
    font-family: "Poppins", sans-serif; font-weight: 300;
    font-size: 17px; color: var(--lime);
  }
</style>
</head>
<body>
<main class="canvas">
  <section class="label label--day" aria-label="Day label">
    <p class="brand">Zeb</p>
    <p class="strength">1500MG</p>
    <p class="spectrum">FULL SPECTRUM</p>
    <div class="product">
      <p class="product__kind">HEMP OIL</p>
      <p class="product__form">EXTRACT</p>
    </div>
    <div class="variant-mark" role="img" aria-label="Day variant icon: leaf with energy bolt"></div>
    <p class="claim">NON-PSYCHOACTIVE</p>
    <p class="volume">30ml</p>
  </section>

  <section class="label label--night" aria-label="Night label">
    <p class="brand">Zeb</p>
    <p class="strength">1500MG</p>
    <p class="spectrum">FULL SPECTRUM</p>
    <div class="product">
      <p class="product__kind">HEMP OIL</p>
      <p class="product__form">EXTRACT</p>
    </div>
    <div class="variant-mark" role="img" aria-label="Night variant icon: moon with stars"></div>
    <p class="claim">NON-PSYCHOACTIVE</p>
    <p class="volume">30ml</p>
  </section>
</main>
</body>
</html>
```